Meridian Sound Wellness LLC Card Design

Need business card with a logo for a hearing aid sales and audiology business. We have two Hearing Instrument Specialists and one Audiologist on staff. Over 25 years in business. Locally owned and operated. Financing available. Most insurances accepted.

Meridian Sound Wellness LLC
48730 W Linden Row, Suite 9
Spokane, WA 99481
509-617-2085
www.meridiansoundnorth.example

Manager
Tobias Wrenfield HIS COHC
License #81729046

Target Market(s)

50yr old + people with a hearing loss.

Industry/Entity Type

Business

Contact Information for Business Card

48730 W Linden Row, Suite 9
Spokane, WA 99481
509-617-2085
www.meridiansoundnorth.example

Manager
Tobias Wrenfield HIS COHC
NRPL #81729046

Font styles to use
Serif
Sans Serif

Requirements
Must have
• Business name, Tobias's name and title(s) and contact information, License #, web address
Nice to have
Should not have

```html
<!DOCTYPE html>
<html lang="en">
<head>
<meta charset="utf-8">
<title>Meridian Sound Wellness – Business Card</title>
<link rel="stylesheet" href="https://fonts.googleapis.com/css2?family=Open+Sans:wght@400;600;700&display=swap">
<style>
  :root {
    --backdrop: #5b3e2c;
    --card: #ffffff;
    --navy: #1f3f8f;
    --blue: #0a6bbd;
    --ink: #2b2b2b;
    --rule: #b9b9b9;
  }
  * { box-sizing: border-box; margin: 0; padding: 0; }
  html, body { width: 1200px; height: 1000px; overflow: hidden; }
  body {
    background: var(--backdrop);
    font-family: "Open Sans", Arial, sans-serif;
    color: var(--ink);
    position: relative;
  }
  .card {
    position: absolute;
    left: 265px;
    width: 666px;
    height: 398px;
    background: var(--card);
    box-shadow: 0 4px 14px rgba(0,0,0,.35);
    overflow: hidden;
  }
  .card--front { top: 73px; }
  .card--back { top: 533px; }

  .brand {
    position: absolute;
    display: flex;
    align-items: center;
    gap: 14px;
    color: var(--navy);
    font-weight: 600;
    line-height: 1.1;
  }
  .brand__dot { border-radius: 50%; background: var(--navy); flex: none; }
  .card--front .brand { left: 32px; top: 40px; font-size: 30px; }
  .card--front .brand__dot { width: 60px; height: 60px; }
  .card--back .brand { left: 135px; top: 127px; font-size: 40px; }
  .card--back .brand__dot { width: 82px; height: 82px; }

  .person {
    position: absolute;
    right: 32px;
    top: 208px;
    text-align: right;
    font-size: 16px;
    line-height: 26px;
  }
  .person__name {
    color: var(--navy);
    font-weight: 700;
    font-size: 20px;
    line-height: 28px;
  }
  .person__creds { color: var(--blue); font-weight: 400; font-size: 16px; }

  .rule {
    position: absolute;
    left: 180px;
    right: 32px;
    top: 240px;
    border-top: 1px solid var(--rule);
  }

  .contact {
    position: absolute;
    left: 33px;
    top: 230px;
    font-size: 16px;
    line-height: 22px;
  }
  .contact__line { display: flex; align-items: center; gap: 6px; height: 24px; }
  .contact__line svg { width: 16px; height: 16px; fill: var(--navy); }
  .contact__address { margin-top: 8px; }
  .contact__company { font-weight: 600; }

  .band {
    position: absolute;
    left: 0; right: 0; bottom: 0;
    height: 23px;
  }
</style>
</head>
<body>

<section class="card card--front">
  <div class="brand">
    <span class="brand__dot"></span>
    <span>Meridian Sound<br>Wellness</span>
  </div>

  <div class="person">
    <div class="person__name">TOBIAS WRENFIELD <span class="person__creds">HIS COHC</span></div>
    <div>Manager</div>
    <div>License #81729046</div>
  </div>
  <div class="rule"></div>

  <div class="contact">
    <div class="contact__line">
      <svg viewBox="0 0 16 16" aria-hidden="true"><path d="M1 6c0-2 3-3 7-3s7 1 7 3v1h-3V5.5C11 5 10 5 8 5s-3 0-4 .5V7H1zM4 8h8l2 5H2z"/></svg>
      <span>509-617-2085</span>
    </div>
    <div class="contact__line">
      <svg viewBox="0 0 16 16" aria-hidden="true"><circle cx="8" cy="8" r="7" fill="none" stroke="#1f3f8f" stroke-width="1.6"/><path d="M1 8h14M8 1c-3 4-3 10 0 14M8 1c3 4 3 10 0 14" fill="none" stroke="#1f3f8f" stroke-width="1.2"/></svg>
      <span>www.meridiansoundnorth.example</span>
    </div>
    <div class="contact__address">
      <div><span class="contact__company">Meridian Sound Wellness</span> LLC</div>
      <div>48730 W Linden Row, Suite 9</div>
      <div>Spokane, WA 99481</div>
    </div>
  </div>

  <svg class="band" viewBox="0 0 666 23" preserveAspectRatio="none" aria-hidden="true">
    <rect x="0" y="0" width="666" height="23" fill="#0a6bbd"/>
    <polygon points="0,0 340,0 318,23 0,23" fill="#1f3f8f"/>
    <polygon points="345,0 352,0 322,23 315,23" fill="#ffffff"/>
  </svg>
</section>

<section class="card card--back">
  <div class="brand">
    <span class="brand__dot"></span>
    <span>Meridian Sound<br>Wellness</span>
  </div>
</section>

</body>
</html>
```